stationery
business cards, letterhead, and envelopes
Professional
Marisol Dunkerly
Mortgage Loan Originator / Owner
418 Kettering Avenue Ste 2270
Makani Falls HI 96799
TideRiverCredit@quillmail.com
www.BrightCedarLending.com
Lowest Rates In Hawaii !!!!!

```html
<!DOCTYPE html>
<html lang="en">
<head>
<meta charset="utf-8">
<title>Marisol Dunkerly – Business Card</title>
<link href="https://fonts.googleapis.com/css2?family=Cinzel:wght@400;600&family=Lato:wght@700&display=swap" rel="stylesheet">
<style>
  :root {
    --page-bg: #e9e6e1;
    --card-white: #ffffff;
    --brand-blue: #3e68b8;
    --brand-green: #1f8a3c;
    --ink-white: #ffffff;
    --ink-soft: #e4ecf8;
  }
  * { margin: 0; padding: 0; box-sizing: border-box; }
  html, body { width: 1200px; height: 914px; overflow: hidden; }
  body {
    background: var(--page-bg);
    position: relative;
    font-family: "Cinzel", serif;
  }
  .business-card {
    position: absolute;
    left: 100px;
    top: 171px;
    width: 1000px;
    height: 572px;
    background: var(--card-white);
    box-shadow: 0 10px 30px rgba(0,0,0,0.18);
    overflow: hidden;
  }
  .card-shapes { position: absolute; inset: 0; }
  .holder-name {
    position: absolute;
    left: 52px;
    top: 52px;
    font-family: "Lato", sans-serif;
    font-weight: 700;
    font-size: 24px;
    color: var(--ink-white);
  }
  .holder-title {
    position: absolute;
    left: 52px;
    top: 86px;
    font-size: 15px;
    letter-spacing: 0.5px;
    color: var(--ink-soft);
  }
  .contact-list {
    position: absolute;
    left: 40px;
    top: 232px;
    list-style: none;
  }
  .contact-item {
    display: flex;
    align-items: center;
    height: 34px;
    font-size: 17px;
    color: var(--ink-white);
    letter-spacing: 0.3px;
    white-space: nowrap;
  }
  .contact-icon {
    width: 22px;
    height: 22px;
    margin-right: 14px;
    flex: none;
  }
  .brand-lockup {
    position: absolute;
    left: 625px;
    top: 262px;
    display: flex;
    align-items: center;
    gap: 16px;
  }
  .brand-mark {
    width: 34px;
    height: 34px;
    border-radius: 50%;
    background: var(--brand-blue);
    flex: none;
  }
  .brand-name {
    font-size: 38px;
    font-weight: 600;
    color: var(--brand-blue);
    letter-spacing: 1px;
    line-height: 1.05;
  }
</style>
</head>
<body>
  <section class="business-card">
    <svg class="card-shapes" width="1000" height="572" viewBox="0 0 1000 572" aria-hidden="true">
      <defs>
        <linearGradient id="panelBlue" x1="0" y1="0" x2="1" y2="1">
          <stop offset="0" stop-color="#5b86cf"/>
          <stop offset="1" stop-color="#3a62b0"/>
        </linearGradient>
      </defs>
      <path d="M0 0 H600 C560 150 540 300 520 572 H0 Z" fill="url(#panelBlue)"/>
      <path d="M640 0 C590 170 570 330 560 572 H543 C553 330 575 170 622 0 Z" fill="var(--brand-green)"/>
    </svg>

    <h1 class="holder-name">Marisol Dunkerly</h1>
    <p class="holder-title">Mortgage Loan Originator / Owner</p>

    <ul class="contact-list">
      <li class="contact-item">
        <svg class="contact-icon" viewBox="0 0 22 22"><circle cx="11" cy="11" r="11" fill="#fff"/><path d="M11 5a4 4 0 0 0-4 4c0 3 4 8 4 8s4-5 4-8a4 4 0 0 0-4-4zm0 5.5a1.5 1.5 0 1 1 0-3 1.5 1.5 0 0 1 0 3z" fill="#3e68b8"/></svg>
        <span>418 Kettering Avenue Ste 2270</span>
      </li>
      <li class="contact-item">
        <span class="contact-icon"></span>
        <span>Makani Falls HI 96799</span>
      </li>
      <li class="contact-item">
        <svg class="contact-icon" viewBox="0 0 22 22"><circle cx="11" cy="11" r="11" fill="#fff"/><path d="M8 6l2 2.5-1.2 1.3a7 7 0 0 0 3.4 3.4L13.5 12 16 14l-1.2 1.8C11 16 6 11 6.2 7.2z" fill="#3e68b8"/></svg>
        <span>(808) 555-0142</span>
      </li>
      <li class="contact-item">
        <svg class="contact-icon" viewBox="0 0 22 22"><circle cx="11" cy="11" r="11" fill="#fff"/><rect x="8" y="5" width="6" height="12" rx="1.2" fill="#3e68b8"/></svg>
        <span>(808) 555-0179</span>
      </li>
      <li class="contact-item">
        <svg class="contact-icon" viewBox="0 0 22 22"><circle cx="11" cy="11" r="11" fill="#fff"/></svg>
        <span>tomkrell88</span>
      </li>
      <li class="contact-item">
        <svg class="contact-icon" viewBox="0 0 22 22"><circle cx="11" cy="11" r="11" fill="#fff"/><rect x="5.5" y="7" width="11" height="8" fill="none" stroke="#3e68b8" stroke-width="1.4"/><path d="M5.5 7l5.5 4.5L16.5 7" fill="none" stroke="#3e68b8" stroke-width="1.4"/></svg>
        <span>TideRiverCredit@quillmail.com</span>
      </li>
      <li class="contact-item">
        <svg class="contact-icon" viewBox="0 0 22 22"><circle cx="11" cy="11" r="11" fill="#fff"/><circle cx="11" cy="11" r="5.5" fill="none" stroke="#3e68b8" stroke-width="1.3"/><path d="M5.5 11h11M11 5.5c-3 3-3 8 0 11M11 5.5c3 3 3 8 0 11" fill="none" stroke="#3e68b8" stroke-width="1.1"/></svg>
        <span>www.BrightCedarLending.com</span>
      </li>
    </ul>

    <div class="brand-lockup">
      <span class="brand-mark"></span>
      <span class="brand-name">Bright Cedar<br>Lending</span>
    </div>
  </section>
</body>
</html>
```